Menu design - professional and sleek design

We need a well presented menu in MS word. Required in MS word so I can easily change and re print as required. This is very important as we change the contents quite often. Attached is the menu design, we are looking for a more sleek design. Information on the attached menu needs to be on the new design.

Requirements
Must have
• Designed to be A4 size on side so it can be folded. Very well formatted so it can be modified and added too.
Nice to have
• Some fun and creativity.

```html
<!DOCTYPE html>
<html lang="en">
<head>
<meta charset="utf-8">
<title>the Heron &amp; Oak — Restaurant Menu</title>
<link rel="stylesheet" href="https://fonts.googleapis.com/css2?family=Arvo&family=Francois+One&family=Josefin+Sans:wght@400&display=swap">
<style>
  :root {
    --backdrop: #d8d8d8;
    --paper: #fdfcf4;
    --ink: #151515;
    --cream: #f7f1d8;
    --flourish-soft: #ecebe2;
  }
  * { box-sizing: border-box; margin: 0; padding: 0; }
  html, body { width: 1056px; height: 1200px; overflow: hidden; background: var(--backdrop); }
  .menu-page {
    position: absolute; left: 104px; top: 0; width: 848px; height: 1200px;
    background: var(--paper); color: var(--ink);
    font-family: "Josefin Sans", sans-serif;
  }
  .brand-name {
    position: absolute; top: 40px; left: 0; width: 100%; text-align: center;
    font-family: "Arvo", serif; font-weight: 400; font-size: 66px; line-height: 1;
    letter-spacing: -1px;
  }
  .brand-name .article { font-size: 44px; }
  .header-flourish {
    position: absolute; top: 132px; width: 96px; height: 72px; border-radius: 8px;
    background: linear-gradient(180deg, var(--paper), var(--flourish-soft));
  }
  .header-flourish.left { left: 96px; }
  .header-flourish.right { right: 96px; }
  .header-rules { position: absolute; left: 0; top: 120px; }
  .title-plate {
    position: absolute; left: 215px; top: 130px; width: 418px; height: 71px;
    background: var(--ink); border-radius: 6px;
    display: flex; align-items: center; justify-content: center;
    font-family: "Francois One", sans-serif; font-size: 50px; letter-spacing: 3px;
    color: var(--cream);
  }
  .title-tab {
    position: absolute; left: 345px; top: 201px; width: 159px; height: 61px;
    background: var(--paper); border: 2px solid var(--ink); border-top: none;
    border-radius: 0 0 14px 14px;
    display: flex; align-items: center; justify-content: center;
    font-family: "Josefin Sans", sans-serif; font-size: 40px; letter-spacing: 2px; padding-top: 6px;
  }
  .column-divider { position: absolute; left: 418px; top: 295px; width: 2px; height: 608px; background: var(--ink); }
  .section-band {
    position: absolute; width: 220px; height: 40px; background: var(--ink); border-radius: 4px;
    display: flex; align-items: center; justify-content: center;
    font-family: "Francois One", sans-serif; font-size: 21px; letter-spacing: 2px; color: var(--cream);
  }
  .dish-list { position: absolute; width: 324px; list-style: none; }
  .dish { display: flex; align-items: baseline; height: 37px; font-size: 18.5px; line-height: 1; }
  .dish .leader { flex: 1; border-bottom: 2px dotted var(--ink); margin: 0 2px 0 10px; transform: translateY(-2px); }
  .dish .price { letter-spacing: 1px; }
  .drinks-rules { position: absolute; inset: 0; }
  .drinks-box {
    position: absolute; left: 62px; top: 961px; width: 725px; height: 186px;
    border: 2px solid var(--ink); border-radius: 12px;
  }
  .drinks-list { position: absolute; list-style: none; width: 315px; top: 32px; }
  .drinks-list .dish { height: 34px; font-size: 18px; }
  .drinks-list .leader { margin-left: 6px; }
</style>
</head>
<body>
<main class="menu-page">
  <h1 class="brand-name"><span class="article">the</span> Heron &amp; Oak</h1>

  <div class="header-flourish left" role="img" aria-label="Decorative flourish beside the title"></div>
  <div class="header-flourish right" role="img" aria-label="Decorative flourish beside the title"></div>
  <svg class="header-rules" width="848" height="150" viewBox="0 120 848 150" fill="none" stroke="var(--ink)" stroke-width="2" aria-hidden="true">
    <path d="M67 220 H339 M67 241 H339 M509 220 H781 M509 241 H781"/>
    <path d="M62 214 v10 M62 236 v10 M786 214 v10 M786 236 v10" stroke-linecap="round"/>
  </svg>
  <div class="title-plate">RESTAURANT</div>
  <div class="title-tab">MENU</div>

  <div class="column-divider"></div>

  <div class="section-band" style="left:120px; top:298px;">STARTERS</div>
  <div class="section-band" style="left:508px; top:298px;">MAIN DISHES</div>
  <div class="section-band" style="left:120px; top:614px;">SANDWICHES</div>
  <div class="section-band" style="left:508px; top:614px;">DESSERTS</div>

  <ul class="dish-list" style="left:68px; top:363px;">
    <li class="dish"><span>NAME OF DISH</span><span class="leader"></span><span class="price">$16</span></li>
    <li class="dish"><span>NAME OF DISH</span><span class="leader"></span><span class="price">$16</span></li>
    <li class="dish"><span>NAME OF DISH</span><span class="leader"></span><span class="price">$16</span></li>
    <li class="dish"><span>NAME OF DISH</span><span class="leader"></span><span class="price">$16</span></li>
    <li class="dish"><span>NAME OF DISH</span><span class="leader"></span><span class="price">$16</span></li>
    <li class="dish"><span>NAME OF DISH</span><span class="leader"></span><span class="price">$16</span></li>
  </ul>
  <ul class="dish-list" style="left:456px; top:363px;">
    <li class="dish"><span>NAME OF DISH</span><span class="leader"></span><span class="price">$16</span></li>
    <li class="dish"><span>NAME OF DISH</span><span class="leader"></span><span class="price">$16</span></li>
    <li class="dish"><span>NAME OF DISH</span><span class="leader"></span><span class="price">$16</span></li>
    <li class="dish"><span>NAME OF DISH</span><span class="leader"></span><span class="price">$16</span></li>
    <li class="dish"><span>NAME OF DISH</span><span class="leader"></span><span class="price">$16</span></li>
    <li class="dish"><span>NAME OF DISH</span><span class="leader"></span><span class="price">$16</span></li>
  </ul>
  <ul class="dish-list" style="left:68px; top:679px;">
    <li class="dish"><span>NAME OF DISH</span><span class="leader"></span><span class="price">$16</span></li>
    <li class="dish"><span>NAME OF DISH</span><span class="leader"></span><span class="price">$16</span></li>
    <li class="dish"><span>NAME OF DISH</span><span class="leader"></span><span class="price">$16</span></li>
    <li class="dish"><span>NAME OF DISH</span><span class="leader"></span><span class="price">$16</span></li>
    <li class="dish"><span>NAME OF DISH</span><span class="leader"></span><span class="price">$16</span></li>
    <li class="dish"><span>NAME OF DISH</span><span class="leader"></span><span class="price">$16</span></li>
  </ul>
  <ul class="dish-list" style="left:456px; top:679px;">
    <li class="dish"><span>NAME OF DISH</span><span class="leader"></span><span class="price">$16</span></li>
    <li class="dish"><span>NAME OF DISH</span><span class="leader"></span><span class="price">$16</span></li>
    <li class="dish"><span>NAME OF DISH</span><span class="leader"></span><span class="price">$16</span></li>
    <li class="dish"><span>NAME OF DISH</span><span class="leader"></span><span class="price">$16</span></li>
    <li class="dish"><span>NAME OF DISH</span><span class="leader"></span><span class="price">$16</span></li>
    <li class="dish"><span>NAME OF DISH</span><span class="leader"></span><span class="price">$16</span></li>
  </ul>

  <svg class="drinks-rules" width="848" height="1200" viewBox="0 0 848 1200" fill="none" stroke="var(--ink)" stroke-width="2" aria-hidden="true">
    <path d="M62 946 H314 M534 946 H787"/>
    <path d="M58 942 v8 M791 942 v8" stroke-linecap="round"/>
    <path d="M62 1161 H787"/>
    <path d="M58 1157 v8 M791 1157 v8" stroke-linecap="round"/>
  </svg>
  <div class="drinks-box">
    <ul class="drinks-list" style="left:20px;">
      <li class="dish"><span>NAME OF DISH</span><span class="leader"></span><span class="price">$16</span></li>
      <li class="dish"><span>NAME OF DISH</span><span class="leader"></span><span class="price">$16</span></li>
      <li class="dish"><span>NAME OF DISH</span><span class="leader"></span><span class="price">$16</span></li>
      <li class="dish"><span>NAME OF DISH</span><span class="leader"></span><span class="price">$16</span></li>
    </ul>
    <ul class="drinks-list" style="left:387px;">
      <li class="dish"><span>NAME OF DISH</span><span class="leader"></span><span class="price">$16</span></li>
      <li class="dish"><span>NAME OF DISH</span><span class="leader"></span><span class="price">$16</span></li>
      <li class="dish"><span>NAME OF DISH</span><span class="leader"></span><span class="price">$16</span></li>
      <li class="dish"><span>NAME OF DISH</span><span class="leader"></span><span class="price">$16</span></li>
    </ul>
  </div>
  <div class="section-band" style="left:324px; top:926px; width:200px;">DRINKS</div>
</main>
</body>
</html>
```